Simple web design project

We need a four page web design for a premier domestic cleaning company. We would like to see designs which use white and blue (the blue in the logo - which is attatched). Please could the tab for the pages be horizontal and at the top of the page. Our company logo is attached and should be included on each page. Ideally, we would like the foundations of each page to be the same, with the word content differing as required (word content attatched). Additionally we have attached a flyer which has been distributed to advertise our company. Please could all web designs illustrate the same professional message this flyer does.

Target Market(s)

females with higher than average income, aged 30-50. Have families and work 9-5.

Industry/Entity Type

It Company

Requirements
Must have
• logo on each page. Foundations of each page the same. phone number and email on the bottom of each page.
Should not have
• please no pictures of females cleaning.

```html
<!DOCTYPE html>
<html lang="en">
<head>
<meta charset="utf-8">
<title>Brookvale Cleaners – Reliable Cleaners</title>
<link rel="stylesheet" href="https://fonts.googleapis.com/css2?family=PT+Sans:wght@700&family=Noto+Sans:wght@400;700&family=Arimo:wght@700&display=swap">
<style>
  :root {
    --blue-light: #4aa6e6;
    --blue-mid: #3a7fd0;
    --blue-deep: #2f6cc4;
    --nav-blue: #2a5fae;
    --nav-edge: #1f4f96;
    --accent-yellow: #f5c518;
    --why-blue: #4488ee;
    --dark: #333333;
    --rule: #6a6a6a;
    --muted: #cfcfcf;
    --white: #ffffff;
  }
  * { margin: 0; padding: 0; box-sizing: border-box; }
  html, body { width: 1200px; height: 1187px; overflow: hidden; background: var(--white); }
  .canvas { position: relative; width: 1200px; height: 1187px; background: var(--white); }
  .page { position: absolute; left: 50px; top: 4px; width: 1096px; height: 1153px; overflow: hidden; }

  .hero { position: absolute; left: 0; top: 0; width: 1096px; height: 805px;
    background: linear-gradient(90deg, var(--blue-light) 0%, var(--blue-mid) 45%, var(--blue-deep) 100%); }
  .hero-art { position: absolute; inset: 0; width: 1096px; height: 805px; }

  .brand { position: absolute; left: 63px; top: 102px; color: var(--white); font-family: "PT Sans", sans-serif; font-weight: 700; }
  .brand-name { display: flex; align-items: center; gap: 12px; font-size: 38px; line-height: 1; }
  .brand-mark { width: 30px; height: 30px; background: var(--white); }
  .brand-tagline { margin: 8px 0 0 68px; font-size: 17px; }

  .headline { position: absolute; left: 0; width: 1096px; top: 232px; text-align: center;
    font-family: "Arimo", sans-serif; font-weight: 700; font-size: 101px; line-height: 1;
    color: var(--white); text-shadow: 2px 4px 6px rgba(0,0,0,0.35); letter-spacing: 1px; }

  .main-nav { position: absolute; left: 218px; top: 339px; width: 791px; height: 35px;
    display: flex; border-radius: 8px; background: linear-gradient(180deg, var(--nav-blue), var(--nav-edge));
    box-shadow: 0 1px 3px rgba(0,0,0,0.3); }
  .main-nav a { flex: 1; display: flex; align-items: center; justify-content: center;
    font-family: "Noto Sans", sans-serif; font-weight: 700; font-size: 15px; color: var(--accent-yellow);
    text-decoration: none; border-left: 1px solid rgba(255,255,255,0.18); }
  .main-nav a:first-child { border-left: none; }

  .why { position: absolute; left: 0; top: 805px; width: 1096px; height: 348px; background: var(--dark);
    font-family: "Noto Sans", sans-serif; color: var(--white); }
  .why-title { position: absolute; left: 172px; top: 30px; font-size: 80px; font-weight: 700;
    color: var(--why-blue); line-height: 1; letter-spacing: 1px; }
  .why-list { position: absolute; left: 184px; top: 123px; display: grid;
    grid-template-columns: 267px auto; row-gap: 17px; list-style: none; font-size: 21px; line-height: 25px; }
  .why-rule { position: absolute; left: 107px; top: 256px; width: 702px; height: 1px; background: var(--rule); }
  .why-cta { position: absolute; left: 183px; top: 278px; font-size: 24px; font-weight: 700; letter-spacing: 1px; }
  .footer-bar { position: absolute; left: 183px; right: 71px; top: 318px; display: flex;
    justify-content: space-between; align-items: center; }
  .footer-contact { font-size: 14px; color: var(--muted); letter-spacing: 0.3px; }
  .footer-nav { display: flex; gap: 23px; }
  .footer-nav a { font-size: 15px; font-weight: 700; color: var(--accent-yellow); text-decoration: none; letter-spacing: 0.5px; }
</style>
</head>
<body>
<div class="canvas">
  <div class="page">
    <header class="hero">
      <svg class="hero-art" viewBox="0 0 1096 805" xmlns="http://www.w3.org/2000/svg">
        <defs>
          <linearGradient id="roomTop" x1="0" y1="0" x2="1" y2="0.4">
            <stop offset="0" stop-color="#8a8784"/>
            <stop offset="0.35" stop-color="#e6e7e8"/>
            <stop offset="0.75" stop-color="#d4d5d6"/>
            <stop offset="1" stop-color="#9c8d7f"/>
          </linearGradient>
          <linearGradient id="roomMain" x1="0" y1="0" x2="0.4" y2="1">
            <stop offset="0" stop-color="#c8c6c2"/>
            <stop offset="0.3" stop-color="#e8e8e6"/>
            <stop offset="0.55" stop-color="#b4aea6"/>
            <stop offset="0.8" stop-color="#a3a4a3"/>
            <stop offset="1" stop-color="#7c7d7b"/>
          </linearGradient>
          <radialGradient id="bucket" cx="0.5" cy="0.5" r="0.5">
            <stop offset="0" stop-color="#2a78dc"/>
            <stop offset="0.6" stop-color="#2f7fe0" stop-opacity="0.7"/>
            <stop offset="1" stop-color="#1d5fb8" stop-opacity="0"/>
          </radialGradient>
        </defs>
        <path d="M354 216 C 450 110, 600 30, 747 0 L 1096 0 L 1096 216 Z" fill="url(#roomTop)"
              role="img" aria-label="Photo of a bright, tidy living room"/>
        <g role="img" aria-label="Photo of a clean modern living room with a bucket of cleaning supplies">
          <path d="M202 360 L 1096 360 L 1096 627 L 840 805 L 143 805 C 105 710, 100 480, 202 360 Z" fill="url(#roomMain)"/>
          <ellipse cx="920" cy="640" rx="165" ry="165" fill="url(#bucket)"/>
        </g>
      </svg>

      <div class="brand">
        <div class="brand-name"><span class="brand-mark"></span>Brookvale Cleaners</div>
        <div class="brand-tagline">Premier Domestic Cleaners</div>
      </div>

      <h1 class="headline">Reliable Cleaners!</h1>

      <nav class="main-nav">
        <a href="#">Home</a>
        <a href="#">Services</a>
        <a href="#">Prices</a>
        <a href="#">Contact</a>
      </nav>
    </header>

    <section class="why">
      <h2 class="why-title">WHY US</h2>
      <ul class="why-list">
        <li>No contracts</li><li>Personalised service</li>
        <li>Insured</li><li>We supply all equipment at no extra cost</li>
        <li>Free quotes</li><li>Hassel free service</li>
      </ul>
      <div class="why-rule"></div>
      <p class="why-cta">Have a look through our website to see how we can help you.</p>
      <footer class="footer-bar">
        <p class="footer-contact">01632 960 418 · hello@brookvalecleaners.co.uk</p>
        <nav class="footer-nav">
          <a href="#">Home</a>
          <a href="#">Services</a>
          <a href="#">Prices</a>
          <a href="#">Contact</a>
        </nav>
      </footer>
    </section>
  </div>
</div>
</body>
</html>
```